Vodka bottle label for premium caribbean market

Label design for a Vodka bottle
Vodka name is 742 Vodka
General colors desired are red and blue
This is a premium vodka product that will be made and distributed in the Caribbean
The art in the background are used in religious celebrations and need to be incorporated
The 742 Vodka design is what I personally created and want to follow a similar art design
Logo should say 742 Vodka

Reason: I was out on leave for personal reasons but ready to make a decision as soon as possible.

Target Market(s)

Premium vodka

Industry/Entity Type

Product

Logo Text

742 Vodka

Font styles to use
Other font styles liked:
• French Script MT

Colors
ec1f27
3176b5

Requirements
Must have
• Incorporate the name 742 Vodka
• Incorporate the 4 art designs as attached
• Font type is provided as an example
• 742 = French Script MT
• Vodka = Footlight MT light
Nice to have
• N/A
Should not have
• N/A

```html
<!DOCTYPE html>
<html lang="en">
<head>
<meta charset="utf-8">
<title>742 Vodka – Bottle Label</title>
<link rel="stylesheet" href="https://fonts.googleapis.com/css2?family=Playfair+Display:wght@700&family=Montserrat:wght@400&display=swap">
<style>
  :root {
    --label-red: #ec1f27;
    --label-blue: #3176b5;
    --rail-gold-dark: #c98a1c;
    --rail-gold-light: #f6d25a;
    --rail-yellow: #ffe11a;
    --brand-gold: #f2c230;
    --ornament-gold: #e9a62c;
    --ink-white: #ffffff;
  }
  html, body {
    margin: 0;
    padding: 0;
    width: 863px;
    height: 1200px;
    overflow: hidden;
    background: #ffffff;
  }
  .label {
    position: relative;
    width: 863px;
    height: 1200px;
    overflow: hidden;
    background: linear-gradient(90deg, var(--label-blue) 7%, var(--label-red) 50%, var(--label-blue) 93%);
  }
  .rail {
    position: absolute;
    top: 0;
    bottom: 0;
  }
  .rail--gold-left { left: 0; width: 51px; background: linear-gradient(160deg, var(--rail-gold-dark), var(--rail-gold-light) 45%, var(--rail-gold-dark)); }
  .rail--yellow-left { left: 51px; width: 13px; background: var(--rail-yellow); }
  .rail--yellow-right { left: 799px; width: 13px; background: var(--rail-yellow); }
  .rail--gold-right { left: 812px; width: 51px; background: linear-gradient(200deg, var(--rail-gold-dark), var(--rail-gold-light) 45%, var(--rail-gold-dark)); }

  .ornament {
    position: absolute;
    border-radius: 50%;
    background: radial-gradient(closest-side, rgba(233,166,44,0.75), rgba(233,166,44,0.35) 60%, rgba(233,166,44,0) 100%);
  }
  .ornament--top-left { left: 110px; top: 50px; width: 305px; height: 220px; }
  .ornament--center { left: 237px; top: 355px; width: 350px; height: 230px; }
  .ornament--bottom-left { left: 135px; top: 595px; width: 255px; height: 255px; }
  .ornament--bottom-right { left: 508px; top: 660px; width: 265px; height: 290px; }
  .crown {
    position: absolute;
    left: 190px; top: 885px;
    width: 102px; height: 75px;
    background: linear-gradient(180deg, var(--rail-gold-light), var(--ornament-gold));
    border-radius: 6px;
    opacity: 0.9;
  }

  .brand-number {
    position: absolute;
    left: 300px;
    width: 260px;
    text-align: center;
    font-family: "Playfair Display", Georgia, serif;
    font-weight: 700;
    font-size: 310px;
    line-height: 1;
    color: var(--brand-gold);
  }
  .brand-number--first { top: 95px; }
  .brand-number--second { top: 355px; }
  .brand-number--third { top: 625px; }

  .tagline {
    position: absolute;
    left: 200px;
    top: 968px;
    width: 455px;
    text-align: center;
    font-family: "Montserrat", Arial, sans-serif;
    font-weight: 400;
    font-size: 42px;
    letter-spacing: 22px;
    text-indent: 22px;
    color: var(--ink-white);
  }
  .brand-word {
    position: absolute;
    left: 190px;
    top: 1008px;
    width: 480px;
    text-align: center;
    font-family: "Playfair Display", Georgia, serif;
    font-weight: 700;
    font-size: 118px;
    line-height: 1;
    color: var(--brand-gold);
  }
</style>
</head>
<body>
  <main class="label">
    <div class="rail rail--gold-left"></div>
    <div class="rail rail--yellow-left"></div>
    <div class="rail rail--yellow-right"></div>
    <div class="rail rail--gold-right"></div>

    <div class="ornament ornament--top-left" role="img" aria-label="Gold ritual vèvè symbol"></div>
    <div class="ornament ornament--center" role="img" aria-label="Gold ritual vèvè symbol with heart grid"></div>
    <div class="ornament ornament--bottom-left" role="img" aria-label="Gold ritual vèvè cross symbol"></div>
    <div class="ornament ornament--bottom-right" role="img" aria-label="Gold ritual vèvè cross symbol"></div>
    <div class="crown" role="img" aria-label="Small gold crown"></div>

    <div class="brand-number brand-number--first">7</div>
    <div class="brand-number brand-number--second">4</div>
    <div class="brand-number brand-number--third">2</div>

    <div class="tagline">PREMIUM</div>
    <div class="brand-word">VODKA</div>
  </main>
</body>
</html>
```